ARC VOLLEY Business Card Project

I'd like to request a business card design for the new company I've launched.
The name of the company is "ARC VOLLEY" an indoor unmanned tennis practice facility.
We would like to see designs that use our brand identity color in the logo I've attached.
We hope to get the design with modern, luxurious and elegant tone and manner.
We hope the logo should not be too big.

Business card must have elements as below:
- Logo (One of the logos I've attached)
- Name (In Korean Text) : 박 서 윤
- Title (In Korean Text) : 대표
- Phone Number : 010-8472-3916
- Email Address : seoyun.park@arcvolley-example.co.kr
- Website : www.arcvolley-example.co.kr
- Instagram : arcvolley
- Address (In Korean text) : 경기도 용인시 수지구 풍덕천로 456 미래타워 5층 501호, 502호

Target Market(s)

Tennis amateurs in 20 to 40s

Industry/Entity Type

Sports, Hobby

Contact Information for Business Card

- Logo (One of the logos I've attached) - Name (In Korean Text) : 박 서 윤 - Title (In Korean Text) : 대표 - Phone Number : 010-8472-3916 - Email Address : seoyun.park@arcvolley-example.co.kr - Website : www.arcvolley-example.co.kr - Instagram : arcvolley - Address (In Korean text) : 경기도 용인시 수지구 풍덕천로 456 미래타워 5층 501호, 502호

Font styles to use
Sans Serif

Requirements
Must have
• Double sided
Nice to have
• Logo with intaglio or relief embossing
Should not have
• Logo should not be too big.

```html
<!DOCTYPE html>
<html lang="ko">
<head>
<meta charset="utf-8">
<title>ARC VOLLEY Business Card</title>
<link rel="stylesheet" href="https://fonts.googleapis.com/css2?family=Noto+Sans+KR:wght@300;400;500&display=swap">
<style>
  :root {
    --backdrop: #6b6b6b;
    --card: #ffffff;
    --brand-green: #2f5237;
    --ink: #333333;
    --card-radius: 22px;
  }
  * { box-sizing: border-box; margin: 0; padding: 0; }
  html, body {
    width: 1200px; height: 967px; overflow: hidden;
    background: var(--backdrop);
    font-family: "Noto Sans KR", sans-serif;
  }
  .stage { position: relative; width: 1200px; height: 967px; }
  .card {
    position: absolute; top: 195px;
    width: 332px; height: 578px;
    background: var(--card);
    border-radius: var(--card-radius);
  }
  .card--front { left: 218px; }
  .card--back { left: 649px; }

  /* front */
  .front-mark {
    position: absolute; left: 114px; top: 42px;
    width: 104px; height: 104px; border-radius: 50%;
    background: var(--brand-green);
  }
  .front-wordmark {
    position: absolute; left: 150px; top: 172px;
    writing-mode: vertical-rl;
    font-size: 40px; font-weight: 400; letter-spacing: 3px;
    color: var(--brand-green); line-height: 1;
  }
  .front-tagline {
    position: absolute; left: 132px; top: 170px;
    writing-mode: vertical-rl;
    display: flex; align-items: center; gap: 6px;
    font-size: 12.5px; font-weight: 400; letter-spacing: 0.5px;
    color: var(--brand-green); line-height: 1;
  }
  .front-tagline__rule {
    display: block; width: 1px; height: 64px;
    background: var(--brand-green);
  }

  /* back */
  .back-logo {
    position: absolute; left: 0; right: 0; top: 52px;
    display: flex; flex-direction: column; align-items: center; gap: 18px;
  }
  .back-logo__circle {
    width: 104px; height: 104px; border-radius: 50%;
    background: var(--brand-green);
  }
  .back-logo__name {
    font-size: 22px; font-weight: 400; letter-spacing: 4px;
    color: var(--brand-green); line-height: 1;
  }
  .person {
    position: absolute; left: 0; right: 0; top: 300px;
    text-align: center;
  }
  .person__name {
    font-size: 22px; font-weight: 500; letter-spacing: 2px;
    color: var(--brand-green); line-height: 1.3;
  }
  .person__title {
    font-size: 13px; font-weight: 400; color: var(--ink); line-height: 1.5;
  }
  .contact-icons {
    position: absolute; left: 0; right: 0; top: 372px;
    display: flex; justify-content: center; gap: 6px;
  }
  .contact-icons svg { width: 16px; height: 16px; display: block; }
  .contact-lines {
    position: absolute; left: 24px; right: 24px; top: 404px;
    text-align: center;
    font-size: 12.5px; font-weight: 400; color: var(--ink); line-height: 20px;
  }
  .contact-lines__address { margin-top: 4px; }
</style>
</head>
<body>
<main class="stage">
  <section class="card card--front" aria-label="Card front">
    <div class="front-mark"></div>
    <div class="front-wordmark">ARC VOLLEY</div>
    <div class="front-tagline">
      <span class="front-tagline__rule"></span>
      <span>ARC YOUR VOLLEY LIFE</span>
      <span class="front-tagline__rule"></span>
    </div>
  </section>

  <section class="card card--back" aria-label="Card back">
    <div class="back-logo">
      <div class="back-logo__circle"></div>
      <div class="back-logo__name">ARC VOLLEY</div>
    </div>

    <div class="person">
      <p class="person__name">박 서 윤</p>
      <p class="person__title">대표</p>
    </div>

    <div class="contact-icons">
      <svg viewBox="0 0 16 16" aria-label="Phone">
        <circle cx="8" cy="8" r="8" fill="#2f5237"/>
        <path d="M5.3 4.2l1.3-.2.7 1.8-.9.7c.4.9 1.1 1.6 2 2l.7-.9 1.8.7-.2 1.3c-.1.4-.5.7-.9.6C7.3 9.9 5.8 8.4 5.4 6.1c-.1-.4.2-.8.6-.9z" fill="#fff" transform="translate(-0.3 0.6)"/>
      </svg>
      <svg viewBox="0 0 16 16" aria-label="Email">
        <circle cx="8" cy="8" r="8" fill="#2f5237"/>
        <rect x="4.2" y="5.3" width="7.6" height="5.4" rx="0.6" fill="#fff"/>
        <path d="M4.4 5.6L8 8.3l3.6-2.7" fill="none" stroke="#2f5237" stroke-width="0.9"/>
      </svg>
      <svg viewBox="0 0 16 16" aria-label="Website">
        <circle cx="8" cy="8" r="8" fill="#2f5237"/>
        <circle cx="8" cy="8" r="3.8" fill="none" stroke="#fff" stroke-width="0.9"/>
        <path d="M4.2 8h7.6M8 4.2c-1.6 2.3-1.6 5.3 0 7.6M8 4.2c1.6 2.3 1.6 5.3 0 7.6" fill="none" stroke="#fff" stroke-width="0.8"/>
      </svg>
      <svg viewBox="0 0 16 16" aria-label="Address">
        <circle cx="8" cy="8" r="8" fill="#2f5237"/>
        <path d="M8 12.2s-3-3.2-3-5.2a3 3 0 0 1 6 0c0 2-3 5.2-3 5.2z" fill="#fff"/>
        <circle cx="8" cy="7" r="1.1" fill="#2f5237"/>
      </svg>
    </div>

    <div class="contact-lines">
      <p>010-8472-3916</p>
      <p>seoyun.park@arcvolley-example.co.kr</p>
      <p>www.arcvolley-example.co.kr</p>
      <p>Instagram @arcvolley</p>
      <p class="contact-lines__address">경기도 용인시 수지구 풍덕천로 456<br>미래타워 5층 501호, 502호</p>
    </div>
  </section>
</main>
</body>
</html>
```